Wordpress and matching prestashop template

Hello
UPDATE
I have bought the plumvale wordpress theme and prestashop theme. I need a cusome skin for them both as below.................
I need a wordpress and and prestashop theme that looks and functions like this http://vantorix.com/demo/wp/plum-vale/ but with my own graphics.
Please study the wordpress design.I need a lively, bright, attractive theme.
I have alphabet characters and animations which must be used to create a theme like this one but with characters and images. I have attached some of them them below. I have uploaded videos of the characters on
http://www.brimwheelgarb.co.uk/imagedump
The theme must also work with prestashop too and match it.
We want to use http://grivaloom.net/theme_previews/7719203-mz-gadget-hut-prestashop-template.
Can you make both templates co-ordinate?
I need a great designer who is creative and understands the brief.
The website title is Zestora Learning
So to summarise i need a wordpress and matching prestashop template designing with the same feel and functionality as the http://vantorix.com/demo/wp/plum-vale/?page_id=392 and http://grivaloom.net/theme_previews/7719203-mz-gadget-hut-prestashop-template but in diffferent colours and images to suit my characters here.
Thank you for reading.
Parents and teachers of young children and children themselves.
Store

```html
<!DOCTYPE html>
<html lang="en">
<head>
<meta charset="utf-8">
<title>Zestora Learning – Shop</title>
<link href="https://fonts.googleapis.com/css2?family=Lobster&family=Arimo:wght@400;700&family=Fredoka:wght@500;600&family=Passion+One:wght@700&family=Kaushan+Script&display=swap" rel="stylesheet">
<style>
:root{
  --earth:#5a3714;
  --sky:#3fb8e6;
  --sky-light:#8fd7f3;
  --grass:#79b41f;
  --grass-dark:#5d9415;
  --pink:#ec6fa6;
  --pink-edge:#f7b7d3;
  --orange:#f08a1c;
  --green-btn:#6aa81e;
  --text:#555;
  --dark:#333;
  --white:#fff;
  --blue-card:#3e9ec4;
}
*{margin:0;padding:0;box-sizing:border-box}
html,body{width:1200px;height:1097px;overflow:hidden}
body{position:relative;font-family:"Arimo",Arial,sans-serif;color:var(--text);
  background:linear-gradient(to bottom,var(--earth) 0,var(--earth) 37px,var(--sky) 37px,var(--sky-light) 150px,var(--grass) 190px,var(--grass-dark) 1031px)}
.abs{position:absolute}
.cloud{position:absolute;background:var(--white);border-radius:40px;opacity:.95}
.logo{left:158px;top:0;width:184px;height:96px;background:#fffbe0;border:3px solid #ffe35a;border-top:none;border-radius:0 0 10px 10px;
  display:flex;align-items:center;justify-content:center;gap:7px}
.logo-dot{width:14px;height:14px;border-radius:50%;background:#e8293b}
.logo-name{font-family:"Arimo",sans-serif;font-weight:700;font-size:17px;color:#e8293b}
.nav a{position:absolute;top:0;display:block;text-decoration:none}
.nav svg{display:block}
.nav span{position:absolute;left:0;right:0;top:14px;text-align:center;font-family:"Lobster",cursive;font-size:24px;color:var(--white);text-shadow:0 1px 2px rgba(0,0,0,.35)}
.kid{position:absolute;border-radius:14px}
.panel{left:166px;top:151px;width:865px;height:867px;background:var(--white);border-radius:6px}
.cart-title{left:180px;top:175px}
.cart-title span{position:absolute;left:0;right:0;top:5px;text-align:center;font-family:"Lobster",cursive;font-size:23px;color:var(--white)}
.item{left:193px;font-size:12px;color:#888}
.item b{color:var(--pink);font-weight:700}
.price{left:193px;font-size:14px;color:var(--dark);font-weight:700}
.totals{left:189px;top:386px;width:228px;font-size:11.5px}
.totals div{display:flex;justify-content:space-between;background:#eef1f1;height:24px;align-items:center;padding:0 10px;margin-bottom:2px}
.totals span:first-child{color:var(--orange);font-weight:700}
.totals span:last-child{color:var(--dark);font-weight:700}
.btnbox{left:187px;top:451px;width:240px;height:51px;background:var(--pink);border:2px solid #d44e94}
.pill{position:absolute;height:30px;border-radius:16px;border:2px solid var(--white);color:var(--white);font-size:14px;display:flex;align-items:center;justify-content:center}
.pill.brown{background:var(--earth)}
.pill.green{background:var(--green-btn)}
.fm-title{left:180px;top:526px;font-family:"Fredoka",sans-serif;font-weight:600;font-size:25px;color:var(--orange);letter-spacing:.5px}
.fm-box{left:180px;top:571px;width:266px;height:78px;border:1px solid #ddd;border-radius:6px;background:#f5f5f5;overflow:hidden}
.fm-price{position:absolute;left:0;top:0;width:110px;height:78px;background:var(--blue-card);color:var(--white);text-align:center;font-family:"Fredoka",sans-serif;font-weight:500;font-size:15px;line-height:16px;padding-top:8px}
.fm-price strong{display:block;font-size:27px;line-height:30px}
.fm-side{position:absolute;left:143px;top:10px;font-family:"Fredoka",sans-serif;font-size:16px;line-height:16px;color:#666}
.fm-side em{font-style:normal;color:var(--blue-card);display:block;margin-top:10px;font-size:16.5px}
.fm-text{left:180px;top:667px;width:262px;font-size:12.5px;line-height:17px;color:#777}
.signup{left:278px;top:735px;width:163px;height:31px;border:3px solid var(--orange);border-radius:6px;background:#f7f7f7;font-size:12.5px;font-weight:700;color:var(--dark);display:flex;align-items:center;gap:10px;padding-left:12px}
.hero{left:467px;top:172px;width:549px;height:364px;border:3px solid #e8e8e8;background:linear-gradient(#9fd9f1,#5fbb3a 35%,#7cc64a 70%,#e9e48f)}
.bar{left:468px;top:556px;width:545px;height:34px;background:linear-gradient(#6e4417,#4d2d0d);border-radius:8px;color:var(--white);font-family:"Fredoka",sans-serif;font-weight:500;font-size:17.5px;letter-spacing:.6px;padding:5px 14px}
.card{top:607px;width:252px;height:173px;border:1px solid #ddd;border-radius:5px;background:linear-gradient(#fff,#eee);overflow:hidden}
.card h3{position:absolute;font-size:13.5px;color:#5b8c12;font-weight:700;white-space:nowrap}
.card p{position:absolute;font-size:11.5px;line-height:15px;color:var(--dark)}
.art{position:absolute;border-radius:8px}
.promo{top:815px;width:267px;height:148px;overflow:hidden}
.sale{left:183px;background:#22c3d2}
.toys{left:463px;background:linear-gradient(#f7a21b,#ee7d10)}
.neque{left:743px;background:linear-gradient(#7cbb21,#5a9316)}
.big{font-family:"Passion One",sans-serif;font-weight:700;color:var(--white);position:absolute}
.small-caps{position:absolute;font-size:10.5px;font-weight:700;color:var(--white);line-height:12px;white-space:nowrap}
.script{font-family:"Kaushan Script",cursive;color:var(--white);position:absolute;white-space:nowrap}
.footer{left:0;top:1031px;width:1200px;height:66px;background:var(--earth);color:var(--white);font-size:12.5px;display:flex;justify-content:center;align-items:center;gap:19px}
</style>
</head>
<body>

<div class="cloud" style="left:30px;top:110px;width:200px;height:26px"></div>
<div class="cloud" style="left:450px;top:85px;width:190px;height:28px"></div>
<div class="cloud" style="left:1075px;top:110px;width:130px;height:24px"></div>

<div class="abs logo"><span class="logo-dot"></span><span class="logo-name">Zestora Learning</span></div>

<nav class="nav">
  <a style="left:373px"><svg width="80" height="76"><polygon points="0,0 80,0 80,76 40,58 0,76" fill="#a3b51b" stroke="#f1e04a" stroke-width="3"/></svg><span>Home</span></a>
  <a style="left:477px"><svg width="87" height="102"><polygon points="0,0 87,0 87,102 43,82 0,102" fill="#1f8fc5" stroke="#0f4f7a" stroke-width="3"/></svg><span style="top:22px">About</span></a>
  <a style="left:594px"><svg width="92" height="80"><polygon points="0,0 92,0 92,80 46,62 0,80" fill="#ffd733" stroke="#f2b40f" stroke-width="3"/></svg><span style="color:#5a3714;text-shadow:none">Gallery</span></a>
  <a style="left:716px"><svg width="81" height="75"><polygon points="0,0 81,0 81,75 40,58 0,75" fill="#8da617" stroke="#f1e04a" stroke-width="3"/></svg><span>Sales</span></a>
  <a style="left:829px"><svg width="74" height="78"><polygon points="0,0 74,0 74,78 37,60 0,78" fill="#ec5fa0" stroke="#f6b0d2" stroke-width="3"/></svg><span>Games</span></a>
  <a style="left:933px"><svg width="98" height="108"><polygon points="0,0 98,0 98,108 49,86 0,108" fill="#d9461b" stroke="#f3a31e" stroke-width="3"/></svg><span style="top:20px">Contact</span></a>
</nav>

<div class="kid" style="left:18px;top:133px;width:155px;height:192px;background:linear-gradient(#f5c85c,#f3e04a)" role="img" aria-label="Illustrated girl with mixing bowl and cat"></div>
<div class="kid" style="left:1018px;top:84px;width:124px;height:187px;background:linear-gradient(#7fa7d8,#b62b45 50%,#5b8bc4)" role="img" aria-label="Illustrated boy on a skateboard"></div>

<div class="abs panel"></div>

<div class="abs cart-title"><svg width="253" height="40"><polygon points="0,0 253,0 245,20 253,40 0,40 8,20" fill="var(--pink)" stroke="#f6c2dc" stroke-width="3"/></svg><span>Shopping Cart</span></div>

<div class="abs item" style="top:237px">1 x <b>Record you daily activity exercise</b></div>
<div class="abs price" style="top:260px">50.00</div>
<div class="abs item" style="top:287px">1 x <b>Record you daily activity exercise</b></div>
<div class="abs price" style="top:311px">50.00</div>
<div class="abs item" style="top:333px">1 x <b>Record you daily activity exercise</b></div>
<div class="abs price" style="top:357px">50.00</div>

<div class="abs totals">
  <div><span>Shipping</span><span>$15.00</span></div>
  <div><span>Total</span><span>$350.00</span></div>
</div>

<div class="abs btnbox">
  <div class="pill brown" style="left:15px;top:8px;width:86px">Cart</div>
  <div class="pill green" style="left:125px;top:8px;width:86px">Checkout</div>
</div>

<div class="abs fm-title">FAMILY MEMBERSHIP</div>
<div class="abs fm-box">
  <div class="fm-price">From<strong>£6.25</strong>a month</div>
  <svg class="abs" style="left:110px;top:0" width="16" height="78"><polygon points="0,0 8,14 0,28 10,40 0,54 8,66 0,78" fill="var(--blue-card)"/></svg>
  <div class="fm-side">No contract<br>or joining fee<em>Learn more</em></div>
</div>
<p class="abs fm-text">From £6.25 per month you will receive Hopwell memberships for you and your family to enjoy, now you can all hop together.</p>
<div class="abs signup"><svg width="16" height="16"><circle cx="8" cy="8" r="8" fill="#eee"/><path d="M3 8h8M8 4l4 4-4 4" stroke="var(--orange)" stroke-width="2" fill="none"/></svg>Sign up your family</div>

<div class="abs hero" role="img" aria-label="Colourful storybook countryside scene with king, queen, animals, farmhouse and river"></div>

<div class="abs bar">Nulla facilisi. Duis aliquet egestas purus in blandit</div>

<div class="abs card" style="left:468px">
  <div class="art" style="left:10px;top:18px;width:100px;height:148px;background:linear-gradient(#f5f5f5,#f2a24a 50%,#3a5fb0)" role="img" aria-label="Letter D character with a child and a dog dancing"></div>
  <h3 style="left:117px;top:20px">Proin gravida nibh</h3>
  <p style="left:122px;top:42px;width:125px">Proin gravida nibh vel velit auctor aliquet. Aenean sollicitudin, lorem quis bibendum auctor,</p>
  <div class="pill green" style="left:154px;top:133px;width:86px;height:30px">Checkout</div>
</div>
<div class="abs card" style="left:757px">
  <div class="art" style="left:142px;top:40px;width:104px;height:128px;background:linear-gradient(#f5f5f5,#7cbc3a 45%,#2c8fd0)" role="img" aria-label="Boy in a striped jumper with a bicycle"></div>
  <h3 style="left:12px;top:22px">Proin gravida nibh</h3>
  <p style="left:14px;top:42px;width:124px;font-size:11px">Proin gravida nibh vel velit auctor aliquet. Aenean sollicitudin, lorem quis bibe ndum auctor,</p>
  <div class="pill" style="left:14px;top:134px;width:72px;height:27px;background:#e6b800;font-weight:700">More...</div>
</div>

<div class="abs promo sale">
  <div class="big" style="left:17px;top:8px;font-size:52px">SALE</div>
  <div class="small-caps" style="left:17px;top:68px">NEQUE PORRO QUISQUAM<br>EST, QUI DOLOREM IPSUM</div>
  <div class="big" style="left:17px;top:92px;font-size:36px">50% OFF</div>
  <div class="art" style="left:180px;top:8px;width:80px;height:136px;background:linear-gradient(#f5a035,#e0701a)" role="img" aria-label="Toy dinosaur"></div>
</div>
<div class="abs promo toys">
  <div class="script" style="left:0;right:0;top:4px;text-align:center;font-size:20px">Nemo enim</div>
  <div class="big" style="left:0;right:0;top:30px;text-align:center;font-size:64px;line-height:64px">TOYS</div>
  <div class="small-caps" style="left:0;right:0;top:97px;text-align:center;font-size:12px;font-weight:400">IPSAM VOLUPTATEM QUIA</div>
  <div class="abs" style="left:79px;top:118px;width:109px;height:25px;background:#ffe022;color:#6b4a0c;font-family:'Passion One',sans-serif;font-size:14px;display:flex;align-items:center;justify-content:center">LEARN MORE ›</div>
</div>
<div class="abs promo neque">
  <div class="art" style="left:188px;top:10px;width:79px;height:138px;background:linear-gradient(#4f8b2a,#3b6e22)" role="img" aria-label="Baby in a dinosaur costume"></div>
  <div class="small-caps" style="left:13px;top:16px;font-size:9.5px;line-height:12px">NEMO ENIM IPSAM VOLUPTATEM<br>QUIA AUT VOLUPTAS SIT ASPE</div>
  <div class="script" style="left:11px;top:50px;font-size:27px">Neque porro</div>
  <div class="small-caps" style="left:13px;top:117px;color:#1d4a08">SHOP NOW ›</div>
</div>

<footer class="abs footer">
  <span>© Copyright Hopwell 2013</span><span>|</span><span>Terms of use</span><span>|</span><span>Privacy Policy</span><span>|</span><span>Accessibility</span><span>|</span><span>Sitemap</span><span>|</span><span>News</span><span>|</span><span>About</span><span>|</span><span>Contact us</span>
</footer>

</body>
</html>
```